business card for Franco-Turkish restaurant

We are a Franco-Turkish restaurant, Le Coquelicot, based in the Cotes d'Armor in Brittany, near the Pink Granite Coast. We serve mainly Turkish cuisine. We would like a card reminding Britain and Turkey. No flag. Color: turquoise (sea ..), green, red. There should be a space for 3 lines: name, address, phone / email

Industry/Entity Type

Fast Food Restaurant

Contact Information for Business Card

Dervan Oruzel
Addresse: 14 Rue Paul-Henri Dauvel, 22410 Kervalou, France
Tel:+33 2 96 47 83 09

Colors
33a6d7
f04a50
acd036

Nice to have
• Symbols of Britain and Turkey
Should not have
• No flags

```html
<!DOCTYPE html>
<html lang="fr">
<head>
<meta charset="utf-8">
<title>Le Coquelicot – Carte de visite</title>
<link rel="stylesheet" href="https://fonts.googleapis.com/css2?family=Open+Sans:wght@400;600;700&display=swap">
<style>
  :root {
    --bg: #e8e5e0;
    --paper: #f4f4f4;
    --turquoise: #33a6d7;
    --poppy: #f04a50;
    --leaf: #acd036;
    --dark: #263238;
    --ink: #2f2f2f;
    --white: #ffffff;
  }
  * { box-sizing: border-box; margin: 0; padding: 0; }
  html, body {
    width: 1200px; height: 1200px; overflow: hidden;
    background: var(--bg);
    font-family: "Open Sans", Arial, sans-serif;
  }
  .canvas { position: relative; width: 1200px; height: 1200px; }

  .card {
    position: absolute; left: 240px; width: 720px; height: 435px;
    background: var(--paper); overflow: hidden;
  }
  .card--front { top: 102px; }
  .card--back  { top: 630px; }

  /* Front */
  .holder { position: absolute; left: 0; top: 0; width: 382px; height: 100%; }
  .holder__name {
    position: absolute; left: 0; width: 100%; top: 112px; text-align: center;
    font-size: 40px; font-weight: 400; color: var(--ink); letter-spacing: -0.3px;
  }
  .holder__role {
    position: absolute; left: 0; width: 100%; top: 170px; text-align: center;
    font-size: 15px; color: var(--poppy); letter-spacing: 0.6px;
  }
  .info-panel {
    position: absolute; left: 382px; top: 0; width: 338px; height: 100%;
    background: var(--turquoise);
  }
  .brand-mark {
    position: absolute; left: 127px; top: 44px; width: 84px; height: 84px;
    border: 6px solid var(--white); border-radius: 50%;
  }
  .brand-name--front {
    position: absolute; left: 0; width: 100%; top: 137px; text-align: center;
    font-size: 20px; font-weight: 400; color: var(--white);
  }
  .contact-row {
    position: absolute; left: 0; width: 100%; height: 61px;
    background: var(--dark);
    clip-path: polygon(0 0, 100% 0, 100% 100%, 0 100%, 22px 50%);
    display: flex; align-items: center; gap: 18px; padding: 0 24px 0 52px;
    color: var(--white); font-weight: 700; font-size: 16px;
  }
  .contact-row--address { top: 194px; font-size: 13px; line-height: 1.35; }
  .contact-row--phone   { top: 270px; }
  .contact-row--web     { top: 345px; }
  .contact-row svg { flex: 0 0 26px; width: 26px; height: 26px; }

  /* Back */
  .brand-mark--back {
    position: absolute; left: 288px; top: 83px; width: 144px; height: 144px;
    border: 10px solid var(--poppy); border-radius: 50%;
  }
  .brand-name--back {
    position: absolute; left: 0; width: 100%; top: 258px; text-align: center;
    font-size: 27px; font-weight: 400; color: var(--dark);
  }
  .sea-edge { position: absolute; left: 0; bottom: 56px; width: 100%; height: 14px; display: block; }
  .web-band {
    position: absolute; left: 0; bottom: 0; width: 100%; height: 58px;
    background: var(--turquoise); color: var(--white);
    display: flex; align-items: center; justify-content: center;
    font-weight: 700; font-size: 19px; letter-spacing: 0.3px;
  }
</style>
</head>
<body>
<div class="canvas">

  <section class="card card--front">
    <div class="holder">
      <p class="holder__name">Dervan Oruzel</p>
      <p class="holder__role">GENERAL MANAGER</p>
    </div>
    <div class="info-panel">
      <div class="brand-mark"></div>
      <p class="brand-name--front">Le Coquelicot</p>

      <div class="contact-row contact-row--address">
        <svg viewBox="0 0 24 24" aria-hidden="true"><path fill="var(--leaf)" d="M12 3 2 12h3v9h5v-6h4v6h5v-9h3z"/></svg>
        <span>14 Rue Paul-Henri Dauvel,<br>22410 Kervalou</span>
      </div>
      <div class="contact-row contact-row--phone">
        <svg viewBox="0 0 24 24" aria-hidden="true"><path fill="var(--leaf)" d="M6.6 10.8a15.1 15.1 0 0 0 6.6 6.6l2.2-2.2c.3-.3.7-.4 1-.2 1.1.4 2.3.6 3.6.6.6 0 1 .4 1 1V20c0 .6-.4 1-1 1A17 17 0 0 1 3 4c0-.6.4-1 1-1h3.5c.6 0 1 .4 1 1 0 1.3.2 2.5.6 3.6.1.3 0 .7-.2 1z"/></svg>
        <span>+33 2 96 47 83 09</span>
      </div>
      <div class="contact-row contact-row--web">
        <svg viewBox="0 0 24 24" aria-hidden="true"><g fill="none" stroke="var(--leaf)" stroke-width="2"><circle cx="12" cy="12" r="9"/><ellipse cx="12" cy="12" rx="4" ry="9"/><path d="M3 12h18M4.5 7.5h15M4.5 16.5h15"/></g></svg>
        <span>www.lecoquelicot.fr</span>
      </div>
    </div>
  </section>

  <section class="card card--back">
    <div class="brand-mark--back"></div>
    <p class="brand-name--back">Le Coquelicot</p>
    <svg class="sea-edge" viewBox="0 0 720 14" preserveAspectRatio="none" aria-hidden="true">
      <path fill="var(--turquoise)" d="M0 8 Q45 0 90 8 T180 8 T270 8 T360 8 T450 8 T540 8 T630 8 T720 8 V14 H0z"/>
    </svg>
    <div class="web-band">www.lecoquelicot.fr</div>
  </section>

</div>
</body>
</html>
```